Litigation Support Company Needing new Simple Web Design

I need to re-design a self done wix hosted website for a small yet nation-wide litigation support consulting firm. I built mine at www.brief-tracer.com myself when I launched but it is very hard on the eyes and needs refreshing/updates. Thanks for taking a look!

Target Market(s)

Law firms and technology experts in the litigation support field.

Number of Pages Required

4 page

Font styles to use
Serif

Colors
f78f20
faa54b
fac994

Requirements
Must have
• Blog, About Us, Services Pages, Crisper Graphics etc.

```html
<!DOCTYPE html>
<html lang="en">
<head>
<meta charset="utf-8">
<title>brief-tracer — Litigation Support</title>
<link rel="stylesheet" href="https://fonts.googleapis.com/css2?family=Lato:wght@400;700;900&display=swap">
<style>
:root{
  --orange:#f78f20;
  --orange-mid:#faa54b;
  --orange-soft:#fac994;
  --ink:#222222;
  --text:#444444;
  --grey-band:#efefef;
  --white:#ffffff;
}
*{box-sizing:border-box;margin:0;padding:0}
html,body{width:1200px;height:2769px;overflow:hidden}
body{position:relative;background:var(--white);font-family:"Lato",Helvetica,Arial,sans-serif;color:var(--text)}
.abs{position:absolute}

/* header */
.site-header{position:absolute;left:0;top:0;width:1200px;height:113px;background:var(--white)}
.brand{position:absolute;display:flex;align-items:center;gap:10px;font-family:"Lato",sans-serif;font-weight:700;color:var(--ink)}
.brand .dot{border-radius:50%;background:var(--orange)}
.brand-header{left:74px;top:26px;font-size:52px}
.brand-header .dot{width:26px;height:26px}
.main-nav a{position:absolute;top:39px;height:39px;line-height:39px;font-size:13px;font-weight:700;color:var(--ink);text-decoration:none;text-transform:uppercase}
.main-nav .active{left:611px;width:90px;text-align:center;background:var(--orange);color:var(--white)}

/* hero */
.hero{position:absolute;left:0;top:113px;width:1200px;height:548px;
  background:radial-gradient(ellipse at 55% 40%,#4c5560 0%,#2c333b 45%,#171b20 100%)}
.hero-brand{left:0;width:1200px;top:150px;justify-content:center;color:var(--white);font-size:118px;font-weight:400}
.hero-brand .dot{width:56px;height:56px}
.hero-tagline{position:absolute;left:0;width:1200px;top:277px;text-align:center;color:var(--white);font-size:24px;letter-spacing:.5px;text-transform:uppercase}
.slider-arrow{position:absolute;top:493px;width:24px;height:24px}

/* section heads */
.section-title{position:absolute;left:0;width:1200px;text-align:center;font-size:28px;font-weight:900;color:var(--ink);text-transform:uppercase}
.title-rule{position:absolute;left:552px;width:96px;height:4px;background:var(--orange)}
.btn{position:absolute;left:510px;width:180px;background:var(--orange);color:var(--white);font-size:15px;font-weight:700;text-align:center;text-transform:uppercase}

/* welcome */
.welcome-copy{position:absolute;left:70px;width:1060px;top:795px;text-align:center;font-size:17px;line-height:28px;color:var(--text)}

/* services */
.services{position:absolute;left:0;top:1019px;width:1200px;height:511px;background:var(--grey-band)}
.service-card{position:absolute;top:1168px;width:328px;height:324px;text-align:center}
.service-card.featured{background:var(--white);box-shadow:0 0 8px rgba(0,0,0,.12)}
.service-icon{position:absolute;left:105px;top:32px;width:118px;height:118px;border-radius:50%;background:var(--orange)}
.service-title{position:absolute;left:10px;width:308px;top:170px;font-size:18px;font-weight:700;line-height:25px;color:var(--orange);text-transform:uppercase}
.service-copy{position:absolute;left:14px;width:300px;top:228px;font-size:15px;line-height:23px;color:var(--text)}

/* blog */
.post{position:absolute;top:1669px;width:330px}
.post-photo{width:330px;height:183px;background:linear-gradient(135deg,#c9ccd0 0%,#8e949a 50%,#5b6168 100%)}
.post-title{margin-top:20px;font-size:18px;font-weight:700;color:var(--orange);text-transform:uppercase}
.post-copy{margin-top:8px;font-size:15px;line-height:23px;color:var(--text)}
.post-meta{margin-top:12px;font-size:14px;color:var(--orange)}

/* contact */
.contact{position:absolute;left:0;top:2064px;width:1200px;height:450px;
  background:linear-gradient(120deg,#f7a75a 0%,#f9bb80 45%,#f6a150 100%)}
.field{position:absolute;border:2px solid var(--white);font-size:12px;color:var(--ink);padding:10px 13px;text-transform:uppercase}

/* footer */
.footer-brand{left:76px;top:2556px;font-size:32px}
.footer-brand .dot{width:16px;height:16px}
.copyright{position:absolute;left:76px;top:2610px;font-size:13px;line-height:22px;color:var(--ink)}
.social{position:absolute;top:2670px;display:flex;gap:18px;left:76px}
.social span{width:18px;height:18px;border-radius:50%;background:#555}
.footer-head{position:absolute;top:2555px;font-size:15px;font-weight:700;color:var(--orange);text-transform:uppercase}
.footer-list{position:absolute;top:2582px;list-style:none;font-size:14px;line-height:28px;color:var(--ink)}
.contact-line{position:absolute;left:596px;display:flex;align-items:center;gap:14px;font-size:14px;color:var(--ink)}
.subscribe-copy{position:absolute;left:884px;top:2582px;width:250px;font-size:14px;line-height:22px;color:var(--ink)}
.subscribe-input{position:absolute;left:884px;top:2642px;width:240px;height:38px;border:1px solid #999;font-size:12px;padding:11px 12px;color:var(--ink)}
.subscribe-btn{position:absolute;left:1036px;top:2690px;width:88px;height:37px;line-height:37px;background:var(--orange);color:var(--white);font-size:12px;font-weight:700;text-align:center;text-transform:uppercase}
</style>
</head>
<body>

<header class="site-header">
  <div class="brand brand-header"><span class="dot"></span>brief-tracer</div>
  <nav class="main-nav">
    <a class="active">Home</a>
    <a style="left:728px">About Us</a>
    <a style="left:845px">Services</a>
    <a style="left:957px">Blog</a>
    <a style="left:1044px">Contact Us</a>
  </nav>
</header>

<section class="hero" role="img" aria-label="Photo of a person in a suit examining a document with a magnifying glass">
  <div class="brand hero-brand abs"><span class="dot"></span>brief-tracer</div>
  <p class="hero-tagline">Don't just review investigate and discover</p>
  <svg class="slider-arrow" style="left:571px" viewBox="0 0 24 24"><circle cx="12" cy="12" r="11" fill="none" stroke="#fff" stroke-width="1.5"/><path d="M14 7l-5 5 5 5" fill="none" stroke="#fff" stroke-width="1.8"/></svg>
  <svg class="slider-arrow" style="left:605px" viewBox="0 0 24 24"><circle cx="12" cy="12" r="11" fill="none" stroke="#fff" stroke-width="1.5"/><path d="M10 7l5 5-5 5" fill="none" stroke="#fff" stroke-width="1.8"/></svg>
</section>

<h2 class="section-title" style="top:707px">Welcome to our website</h2>
<div class="title-rule" style="top:764px"></div>
<p class="welcome-copy">I believe that proper application of technology can make or break the discovery process of small and large matters alike.&nbsp; Document review projects can create endless headaches without proper strategy and it is my goal to analyze every project individually and apply the proper level of technology to fit the client's needs.</p>
<div class="btn" style="top:917px;height:45px;line-height:45px">Read More</div>

<section class="services"></section>
<h2 class="section-title" style="top:1067px">Our Services</h2>
<div class="title-rule" style="top:1122px"></div>

<div class="service-card featured" style="left:76px">
  <svg class="service-icon" viewBox="0 0 118 118"><circle cx="59" cy="59" r="59" fill="#f78f20"/><circle cx="57" cy="62" r="24" fill="#fff"/><path d="M57 62V38A24 24 0 0 1 81 62Z" fill="#f78f20"/><path d="M62 57V33A24 24 0 0 1 86 57Z" fill="#fff"/><path d="M57 62L40 79" stroke="#f78f20" stroke-width="3"/></svg>
  <div class="service-title">Received Data Discovery<br>Review Management</div>
  <p class="service-copy">Aliquam molestie, mi et imperdiet euismod, dui purus auctor tellus, et interdum lacus lectus et ante lobortis...</p>
</div>
<div class="service-card" style="left:436px">
  <svg class="service-icon" viewBox="0 0 118 118"><circle cx="59" cy="59" r="59" fill="#f78f20"/><ellipse cx="52" cy="54" rx="20" ry="14" fill="#fff"/><path d="M40 64l-6 10 14-6Z" fill="#fff"/><ellipse cx="68" cy="64" rx="18" ry="13" fill="#fff" stroke="#f78f20" stroke-width="3"/><path d="M80 72l6 9-13-5Z" fill="#fff"/></svg>
  <div class="service-title">Managed Litigation<br>Support</div>
  <p class="service-copy">Aliquam molestie, mi et imperdiet euismod, dui purus auctor tellus, et interdum lacus lectus et ante lobortis...</p>
</div>
<div class="service-card" style="left:796px">
  <svg class="service-icon" viewBox="0 0 118 118"><circle cx="59" cy="59" r="59" fill="#f78f20"/><circle cx="54" cy="54" r="15" fill="none" stroke="#fff" stroke-width="7"/><path d="M65 65l14 14" stroke="#fff" stroke-width="9" stroke-linecap="round"/></svg>
  <div class="service-title">Pre-Discovery Strategy and<br>Support Services</div>
  <p class="service-copy">Aliquam molestie, mi et imperdiet euismod, dui purus auctor tellus, et interdum lacus lectus et ante lobortis...</p>
</div>

<h2 class="section-title" style="top:1566px">Blog Posts</h2>
<div class="title-rule" style="top:1623px"></div>

<article class="post" style="left:76px">
  <div class="post-photo" role="img" aria-label="Photo of colleagues reviewing papers in an office"></div>
  <h3 class="post-title">Nam Fermentum Vestibulum</h3>
  <p class="post-copy">Aliquam molestie, mi et imperdiet euismod, dui purus auctor tellus, et interdum lacus lectus et ante lobortis turpis in&nbsp; odio blandit ac..</p>
  <p class="post-meta">Aug 30, 2018&nbsp; |&nbsp; By Admin</p>
</article>
<article class="post" style="left:434px">
  <div class="post-photo" role="img" aria-label="Photo of two professionals discussing work at a computer"></div>
  <h3 class="post-title">Nam Fermentum Vestibulum</h3>
  <p class="post-copy">Aliquam molestie, mi et imperdiet euismod, dui purus auctor tellus, et interdum lacus lectus et ante lobortis turpis in&nbsp; odio blandit ac..</p>
  <p class="post-meta">Aug 30, 2018&nbsp; |&nbsp; By Admin</p>
</article>
<article class="post" style="left:796px">
  <div class="post-photo" role="img" aria-label="Photo of a team planning at a board covered in notes"></div>
  <h3 class="post-title">Nam Fermentum Vestibulum</h3>
  <p class="post-copy">Aliquam molestie, mi et imperdiet euismod, dui purus auctor tellus, et interdum lacus lectus et ante lobortis turpis in&nbsp; odio blandit ac..</p>
  <p class="post-meta">Aug 30, 2018&nbsp; |&nbsp; By Admin</p>
</article>

<section class="contact" role="img" aria-label="Orange-toned photo of hands writing on paper behind the contact form"></section>
<h2 class="section-title" style="top:2112px">Contact Us</h2>
<div class="title-rule" style="top:2169px"></div>
<div class="field" style="left:255px;top:2211px;width:330px;height:41px">Name</div>
<div class="field" style="left:613px;top:2211px;width:332px;height:41px">Email Address</div>
<div class="field" style="left:255px;top:2265px;width:330px;height:41px">Phone No</div>
<div class="field" style="left:613px;top:2265px;width:332px;height:41px">Subject</div>
<div class="field" style="left:255px;top:2319px;width:690px;height:79px">Message</div>
<div class="btn" style="top:2420px;height:44px;line-height:44px">Submit</div>

<footer>
  <div class="brand footer-brand abs"><span class="dot"></span>brief-tracer</div>
  <p class="copyright">Copyright © 2018. Company Name<br>All Right Reserved</p>
  <div class="social" aria-label="Social links"><span></span><span></span><span></span><span></span><span></span><span></span></div>

  <h4 class="footer-head" style="left:367px">Site Map</h4>
  <ul class="footer-list" style="left:367px">
    <li>Home</li><li>About us</li><li>Services</li><li>Blog</li><li>Contact us</li>
  </ul>

  <h4 class="footer-head" style="left:596px">Contact Address</h4>
  <p class="abs" style="left:596px;top:2582px;font-size:14px;line-height:26px;color:var(--ink)">1450 Harbor Point Rd<br>Lakeview Prairie,<br>MO 63300</p>
  <div class="contact-line" style="top:2660px">
    <svg width="14" height="14" viewBox="0 0 24 24"><path d="M6.6 10.8a15 15 0 0 0 6.6 6.6l2.2-2.2a1 1 0 0 1 1-.25 11.4 11.4 0 0 0 3.6.57 1 1 0 0 1 1 1V20a1 1 0 0 1-1 1A17 17 0 0 1 3 4a1 1 0 0 1 1-1h3.5a1 1 0 0 1 1 1c0 1.25.2 2.45.57 3.57a1 1 0 0 1-.25 1Z" fill="#333"/></svg>
    1-800-555-0142</div>
  <div class="contact-line" style="top:2691px">
    <svg width="14" height="12" viewBox="0 0 24 20"><rect x="1" y="2" width="22" height="16" fill="#333"/><path d="M1 3l11 8 11-8" fill="none" stroke="#fff" stroke-width="2"/></svg>
    info@brief-tracer.com</div>

  <h4 class="footer-head" style="left:884px">Email Subscribe</h4>
  <p class="subscribe-copy">Vestibulum ante ipsum primis in faucibus orci luctus..</p>
  <div class="subscribe-input">Enter Email Address</div>
  <div class="subscribe-btn">Sign Up</div>
</footer>

</body>
</html>
```